Product Label Design

We require 2 labels, with the same look and feel, designed for our range of trucking related products for the transport industry. Our logo has been provided.

In terms of the look and feel, we are after:
- a clean and elegant design to represent our premium range of products. By clean we mean not "too busy" or cluttered
- masculine as this relates to trucking,
- must convey that our products are cutting-edge and innovative (our competitors' labels are outdated and dull thus we want to stand-out in the world market)

We want you to create a standardised label template for us, which we can use for several products. We will simply change the product description and product code and reprint.

Each product label will have a:
• Product Description
• Product code
• An image or artwork of a truck as all our products are for the transport industry
• Display product Size in bottom right hand corner
Label 1: 20L (180 mm x 180 mm with 5 mm radius on corners )
Label 2: 750ml (A copy of the 750ml bottle die line has been unloaded as a PDF)

You may use text placeholders for the description.

Files Required:
We need the final design as a psd file, as our business uses Photoshop CS6.

REFERENCE:
Attached is an sample label with the features we want (ie product description, product size, and so on). Please DO NOT use or see this as a reference for your design or style we are after. We do not want your creativity to be restricted by this sample.

Target Market(s)

Products for the trucking industry

Industry/Entity Type

Industry

Colors

Designer to choose colors to be used in the design.

Requirements
Must have
• Logo
• • Image of a truck on the label (preferably the truck should be cutting edge and modern to align it with our product)
• • Some type of background
• • Product description
• • Product code
• • Product size on Bottom Right corner
Should not have
• Unnecessary graphics that will clutter the design

```html
<!DOCTYPE html>
<html lang="en">
<head>
<meta charset="utf-8">
<title>Halvern Freight – Engine Oil Labels</title>
<link rel="stylesheet" href="https://fonts.googleapis.com/css2?family=Michroma&family=Oswald:wght@300;500;600&family=Quicksand:wght@500&display=swap">
<style>
  :root {
    --page-bg: #e3e5e8;
    --label-black: #121212;
    --label-dark: #1d1d1d;
    --stripe: #262626;
    --gold: #d99a4f;
    --gold-light: #f2c48d;
    --gold-deep: #a8652b;
    --red: #d8202a;
    --yellow: #f4b21c;
    --white: #f4f4f4;
    --caption: #5a5f66;
  }
  * { box-sizing: border-box; margin: 0; padding: 0; }
  html, body { width: 1200px; height: 824px; overflow: hidden; }
  body {
    background: linear-gradient(180deg, #d7dade 0%, var(--page-bg) 60%, #eceef0 100%);
    position: relative;
    font-family: "Oswald", sans-serif;
  }

  /* ---------- label frames ---------- */
  .label {
    position: absolute;
    width: 530px;
    background:
      repeating-linear-gradient(0deg, rgba(255,255,255,0.025) 0 1px, transparent 1px 4px),
      linear-gradient(160deg, var(--label-dark) 0%, var(--label-black) 55%, #0b0b0b 100%);
    overflow: hidden;
    color: var(--white);
  }
  .label--drum { left: 613px; top: 198px; height: 530px; border-radius: 12px; }
  .label--bottle {
    left: 120px; top: 258px; height: 570px;
    transform: scale(0.77); transform-origin: 0 0;
    clip-path: polygon(14% 0, 86% 0, 100% 10%, 100% 100%, 0 100%, 0 10%);
    border-radius: 0 0 10px 10px;
  }

  .label__backdrop {
    position: absolute; left: 0; right: 0; top: 190px; height: 260px;
    background: linear-gradient(170deg, transparent 0%, rgba(70,70,70,0.35) 40%, rgba(40,40,40,0.25) 60%, transparent 100%);
  }

  /* ---------- brand ---------- */
  .brand {
    position: absolute; top: 40px; left: 0; right: 0;
    display: flex; justify-content: center; align-items: center; gap: 10px;
  }
  .brand__dot { width: 34px; height: 34px; border-radius: 50%; background: var(--gold); }
  .brand__name {
    font-family: "Oswald", sans-serif; font-weight: 600; font-size: 26px;
    line-height: 1; letter-spacing: 1px; color: var(--gold);
  }

  /* ---------- titles ---------- */
  .rule {
    position: absolute; left: 90px; right: 90px; height: 1px;
    background: linear-gradient(90deg, transparent, var(--gold-deep), var(--gold-light), var(--gold-deep), transparent);
  }
  .rule--top { top: 117px; }
  .rule--mid { top: 192px; }
  .rule--low { top: 243px; }

  .product-title {
    position: absolute; top: 124px; left: 0; right: 0; text-align: center;
    font-family: "Michroma", sans-serif; font-size: 56px; line-height: 64px; letter-spacing: 1px;
    background: linear-gradient(180deg, var(--gold-light) 0%, var(--gold) 45%, var(--gold-deep) 100%);
    -webkit-background-clip: text; background-clip: text; color: transparent;
  }
  .product-name {
    position: absolute; top: 196px; left: 0; right: 0; text-align: center;
    font-family: "Oswald", sans-serif; font-weight: 300; font-size: 38px; line-height: 44px;
    color: var(--red); letter-spacing: 0.5px;
  }
  .product-desc {
    position: absolute; top: 262px; left: 0; right: 0; text-align: center;
    font-family: "Quicksand", sans-serif; font-weight: 500; font-size: 9px;
    line-height: 10px; letter-spacing: 2px; color: var(--white);
  }

  /* ---------- spec ---------- */
  .spec { position: absolute; top: 300px; left: 0; right: 0; text-align: center; }
  .spec__type { font-weight: 500; font-size: 11px; line-height: 14px; color: var(--white); }
  .spec__grade { font-weight: 600; font-size: 33px; line-height: 36px; color: var(--yellow); }
  .spec__grade small { font-size: 9px; color: var(--yellow); vertical-align: 18px; margin-right: 4px; }
  .spec__api { font-weight: 500; font-size: 13px; line-height: 16px; color: var(--white); }
  .spec__api small { font-size: 6px; vertical-align: 5px; margin-right: 3px; }

  /* ---------- artwork & size ---------- */
  .truck-art {
    position: absolute; left: 118px; right: 0; top: 360px; height: 165px;
    background: linear-gradient(180deg, #c9cbcd 0%, #9c9fa2 55%, #3a3a3a 100%);
    border-radius: 4px 0 0 0;
  }
  .size {
    position: absolute; left: 28px; bottom: 24px;
    font-weight: 500; font-size: 28px; line-height: 30px; color: var(--white);
  }

  .caption {
    position: absolute; left: 613px; width: 530px; top: 738px; text-align: center;
    font-weight: 500; font-size: 19px; color: var(--caption);
  }
</style>
</head>
<body>

<section class="label label--bottle" aria-label="750 ml bottle label">
  <div class="label__backdrop"></div>
  <div class="brand"><span class="brand__dot"></span><span class="brand__name">HALVERN<br>FREIGHT</span></div>
  <div class="rule rule--top"></div>
  <h1 class="product-title">PRODUCT</h1>
  <div class="rule rule--mid"></div>
  <p class="product-name">PRODUCT NAME HERE</p>
  <div class="rule rule--low"></div>
  <p class="product-desc">Lorem ipsum dolor sit amet.<br>Dolor sit amet.</p>
  <div class="spec">
    <p class="spec__type">Engine Oil</p>
    <p class="spec__grade"><small>SAE</small>20W-50</p>
    <p class="spec__api"><small>API</small>SG/CO</p>
  </div>
  <div class="truck-art" role="img" aria-label="Photo of modern white box trucks in a row"></div>
  <p class="size">750ML</p>
</section>

<section class="label label--drum" aria-label="20 litre drum label">
  <div class="label__backdrop"></div>
  <div class="brand"><span class="brand__dot"></span><span class="brand__name">HALVERN<br>FREIGHT</span></div>
  <div class="rule rule--top"></div>
  <h1 class="product-title">PRODUCT</h1>
  <div class="rule rule--mid"></div>
  <p class="product-name">PRODUCT NAME HERE</p>
  <div class="rule rule--low"></div>
  <p class="product-desc">Lorem ipsum dolor sit amet.<br>Dolor sit amet.</p>
  <div class="spec">
    <p class="spec__type">Engine Oil</p>
    <p class="spec__grade"><small>SAE</small>20W-50</p>
    <p class="spec__api"><small>API</small>SG/CO</p>
  </div>
  <div class="truck-art" role="img" aria-label="Photo of modern white box trucks in a row"></div>
  <p class="size">20L</p>
</section>

<p class="caption">180 mm x 180 mm</p>

</body>
</html>
```